New world-class investment firm needs a business card design

We need a business card design for a new investment firm called 'Dalvin Soeurs & Company.' We acquire companies in the media sector and secure funding from conservative ultra, high-net worth individuals. We would like a black and white color design. We are seeking classic, elegant, and sophisticated designs. The final design should communicate financial safety, class, timelessness, and highly ethical. On the back of the business card, we would simply like the lion logo to be centered. I have attached a mock card, and variations on it are welcomed.
Industry/Entity Type
Conservative
Font styles to use
Other font styles liked:
- Garamond
Look and feel
Each slider illustrates characteristics of the customer's brand and the style your logo design should communicate.

```html
<!DOCTYPE html>
<html lang="en">
<head>
<meta charset="utf-8">
<title>Dalvin Soeurs &amp; Company — Business Card Proposals</title>
<link rel="stylesheet" href="https://fonts.googleapis.com/css2?family=Arimo:wght@700&family=Open+Sans:wght@600;700&family=Noto+Serif:wght@400;700&family=Montserrat:wght@500&display=swap">
<style>
  :root {
    --teal: #47b1c3;
    --teal-text: #4aa9bb;
    --ink: #1f2729;
    --white: #ffffff;
    --label-pink: #d6246e;
    --label-red: #d62f3a;
    --bar-grey: #88888c;
    --muted: #6b6b6b;
    --charcoal: #262626;
    --seal-light: #b9bcbf;
    --seal-teal: #5c9da6;
    --seal-dark: #55595b;
  }
  * { margin: 0; padding: 0; box-sizing: border-box; }
  html, body { width: 1200px; height: 812px; overflow: hidden; background: var(--white); }
  .sheet { position: relative; width: 1200px; height: 812px; }

  .label { position: absolute; font-family: "Arimo", Arial, sans-serif; font-weight: 700; transform: translateX(-50%); white-space: nowrap; }
  .label--side { font-size: 20px; color: var(--label-pink); }
  .label--sample { font-size: 22px; color: var(--label-red); }

  .card { position: absolute; overflow: hidden; }
  .serif { font-family: "Noto Serif", Georgia, serif; }
  .sans { font-family: "Open Sans", Arial, sans-serif; }
  .abs { position: absolute; white-space: nowrap; }
  .center { transform: translateX(-50%); text-align: center; }

  .seal { position: absolute; border-radius: 50%; }

  /* Sample 1 front */
  .front-teal { left: 57px; top: 70px; width: 539px; height: 314px; background: var(--white); }
  .front-teal .edge { position: absolute; left: 0; top: 0; width: 20px; height: 100%; background: var(--teal); }
  .front-teal .panel { position: absolute; left: 162px; top: 0; width: 377px; height: 100%; background: var(--teal); }
  .front-teal .city-band { position: absolute; left: 162px; top: 73px; width: 377px; height: 22px; background: var(--white); }
  .front-teal .firm { left: 182px; top: 32px; font-size: 28px; font-weight: 700; color: var(--ink); letter-spacing: -0.3px; }
  .front-teal .cities { left: 182px; top: 76px; font-size: 13px; color: var(--teal-text); }
  .front-teal .person { left: 182px; top: 171px; font-size: 22px; font-weight: 700; color: var(--white); }
  .front-teal .role { left: 182px; top: 199px; font-size: 13px; color: var(--white); }
  .front-teal .contact { left: 182px; top: 243px; font-size: 13.5px; line-height: 19px; color: var(--white); }
  .front-teal .seal { left: 40px; top: 95px; width: 100px; height: 100px; background: var(--seal-light); }
  .front-teal .seal-name { left: 91px; top: 204px; font-size: 10px; font-weight: 700; color: var(--muted); }

  /* Sample 1 back */
  .back-teal { left: 622px; top: 70px; width: 539px; height: 314px; background: var(--teal); }
  .back-teal .seal { left: 193px; top: 65px; width: 150px; height: 150px; background: var(--seal-teal); }
  .back-teal .wordmark { left: 269px; top: 236px; font-family: "Montserrat", Arial, sans-serif; font-weight: 500; font-size: 19px; letter-spacing: 1.6px; color: var(--white); }

  /* Sample 2 front */
  .front-white { left: 57px; top: 490px; width: 539px; height: 270px; background: var(--white); }
  .front-white .firm { left: 270px; top: 0; font-size: 28px; font-weight: 700; color: var(--ink); letter-spacing: -0.3px; }
  .front-white .rule { position: absolute; top: 45px; height: 12px; background: var(--bar-grey); }
  .front-white .rule--left { left: 0; width: 162px; }
  .front-white .rule--right { left: 376px; width: 163px; }
  .front-white .cities { left: 270px; top: 42px; font-size: 13px; color: var(--muted); }
  .front-white .seal { left: 222px; top: 78px; width: 96px; height: 96px; background: var(--seal-light); }
  .front-white .seal-name { left: 270px; top: 180px; font-size: 10px; font-weight: 700; color: var(--muted); }
  .front-white .person { left: 270px; top: 209px; font-size: 22px; font-weight: 700; color: var(--ink); }
  .front-white .role { left: 270px; top: 237px; font-size: 13px; color: var(--muted); }

  /* Sample 2 back */
  .back-dark { left: 622px; top: 466px; width: 539px; height: 314px; background: var(--charcoal); }
  .back-dark .seal { left: 193px; top: 42px; width: 150px; height: 150px; background: var(--seal-dark); }
  .back-dark .seal-name { left: 269px; top: 200px; font-size: 11px; font-weight: 700; color: var(--seal-light); }
  .back-dark .contact-line { left: 269px; font-size: 15px; color: var(--white); display: flex; align-items: center; gap: 8px; }
  .back-dark .contact-line--phone { top: 227px; }
  .back-dark .contact-line--mail { top: 248px; }
  .icon { width: 12px; height: 12px; }
</style>
</head>
<body>
<main class="sheet">
  <div class="label label--side" style="left:328px; top:36px;">Front</div>
  <div class="label label--sample" style="left:565px; top:33px;">Sample No. 1</div>
  <div class="label label--side" style="left:892px; top:36px;">Back</div>

  <section class="card front-teal" aria-label="Sample 1 front">
    <div class="edge"></div>
    <div class="panel"></div>
    <div class="city-band"></div>
    <div class="seal" role="img" aria-label="Dalvin Soeurs seal"></div>
    <div class="abs center serif seal-name">Dalvin Soeurs &amp; Co.</div>
    <div class="abs sans firm">Dalvin Soeurs &amp; Co.</div>
    <div class="abs serif cities">New York &bull; Los Angles &bull; Geneva</div>
    <div class="abs serif person">Laurent T. Dalvin</div>
    <div class="abs serif role">Chairman &amp; CEO</div>
    <div class="abs serif contact">917-555-0142<br>laurent@dalvinsoeurs.com</div>
  </section>

  <section class="card back-teal" aria-label="Sample 1 back">
    <div class="seal" role="img" aria-label="Dalvin Soeurs seal"></div>
    <div class="abs center wordmark">DALVIN SOEURS &amp; COMPANY</div>
  </section>

  <div class="label label--side" style="left:328px; top:433px;">Front</div>
  <div class="label label--sample" style="left:565px; top:430px;">Sample No. 2</div>
  <div class="label label--side" style="left:892px; top:433px;">Back</div>

  <section class="card front-white" aria-label="Sample 2 front">
    <div class="abs center sans firm">Dalvin Soeurs &amp; Company</div>
    <div class="rule rule--left"></div>
    <div class="rule rule--right"></div>
    <div class="abs center serif cities">New York &bull; Los Angles &bull; Geneva</div>
    <div class="seal" role="img" aria-label="Dalvin Soeurs seal"></div>
    <div class="abs center serif seal-name">Dalvin Soeurs &amp; Company</div>
    <div class="abs center serif person">Laurent T. Dalvin</div>
    <div class="abs center serif role">Chairman &amp; CEO</div>
  </section>

  <section class="card back-dark" aria-label="Sample 2 back">
    <div class="seal" role="img" aria-label="Dalvin Soeurs seal"></div>
    <div class="abs center serif seal-name">Dalvin Soeurs &amp; Company</div>
    <div class="abs center serif contact-line contact-line--phone">
      <svg class="icon" viewBox="0 0 12 12" aria-hidden="true"><path d="M4 1.5 L5.2 1.5 L5.6 3.8 L4.6 4.6 Q5 7 7.4 7.4 L8.2 6.4 L10.5 6.8 L10.5 8 Q10 10.5 7.5 10 Q2.5 8.5 2 4.5 Q1.8 2 4 1.5 Z" fill="#ffffff"/></svg>
      <span>917-555-0142</span>
    </div>
    <div class="abs center serif contact-line contact-line--mail">
      <svg class="icon" viewBox="0 0 12 12" aria-hidden="true"><rect x="0.75" y="2.25" width="10.5" height="7.5" fill="none" stroke="#ffffff" stroke-width="1"/><path d="M1 2.5 L6 6.5 L11 2.5" fill="none" stroke="#ffffff" stroke-width="1"/></svg>
      <span>laurent@dalvinsoeurs.com</span>
    </div>
  </section>
</main>
</body>
</html>
```